Talvex Industrial Maintenance Business Card

Design a business card with the following information, logo must be included.
Talvex Industrial Maintenance
Dale Virnow Jr.
Pone 413-627-8154
email dale.virnow.jr@brindlemail.net

```html
<!DOCTYPE html>
<html lang="en">
<head>
<meta charset="utf-8">
<title>Talvex Industrial Maintenance – Business Card</title>
<link href="https://fonts.googleapis.com/css2?family=Montserrat:wght@600;700&family=Arimo&display=swap" rel="stylesheet">
<style>
  :root {
    --brand-blue: #0a73b9;
    --ink: #2a2a2a;
    --rule-grey: #8a8a8a;
    --wave-grey: #7d7d7d;
    --backdrop: #9b9b9b;
    --paper: #ffffff;
  }
  * { margin: 0; padding: 0; box-sizing: border-box; }
  html, body { width: 1021px; height: 1200px; overflow: hidden; }
  body { background: var(--backdrop); position: relative; }

  .card {
    position: absolute;
    width: 753px;
    height: 429px;
    overflow: hidden;
  }
  .card--front { left: 134px; top: 119px; background: var(--paper); }
  .card--back  { left: 131px; top: 651px; background: var(--brand-blue); }

  .wave { position: absolute; inset: 0; width: 753px; height: 429px; }

  .wordmark {
    position: absolute;
    display: flex;
    align-items: center;
    font-family: "Montserrat", sans-serif;
    font-weight: 600;
  }
  .wordmark__dot { border-radius: 50%; flex: none; }
  .wordmark__text { display: flex; flex-direction: column; line-height: 1; }

  .card--front .wordmark { left: 66px; top: 170px; gap: 14px; color: var(--brand-blue); }
  .card--front .wordmark__dot { width: 60px; height: 60px; background: var(--brand-blue); }
  .card--front .wordmark__name { font-size: 47px; letter-spacing: 0.5px; }
  .card--front .wordmark__tagline { font-size: 13.2px; margin-top: 6px; }

  .divider {
    position: absolute;
    left: 376px; top: 157px;
    width: 1.5px; height: 116px;
    background: var(--rule-grey);
  }

  .contact { position: absolute; left: 407px; top: 152px; }
  .contact__name {
    font-family: "Montserrat", sans-serif;
    font-weight: 700;
    font-size: 29px;
    color: var(--brand-blue);
    letter-spacing: 0.3px;
    margin-left: 1px;
    margin-bottom: 12px;
  }
  .contact__list { list-style: none; }
  .contact__item {
    display: flex;
    align-items: center;
    gap: 9px;
    height: 26.5px;
    font-family: "Arimo", sans-serif;
    font-size: 19px;
    color: var(--ink);
  }
  .contact__icon { width: 17px; height: 17px; flex: none; fill: var(--brand-blue); }

  .card--back .wordmark { left: 151px; top: 150px; gap: 22px; color: var(--paper); }
  .card--back .wordmark__dot { width: 118px; height: 118px; background: var(--paper); }
  .card--back .wordmark__name { font-size: 86px; letter-spacing: 1px; }
  .card--back .wordmark__tagline { font-size: 22.5px; margin-top: 8px; }
</style>
</head>
<body>

<section class="card card--front" aria-label="Business card front">
  <svg class="wave" viewBox="0 0 753 429" aria-hidden="true">
    <path fill="var(--wave-grey)" d="M0 334 C70 430 260 412 430 392 C560 377 700 352 753 392 L753 429 L0 429 Z"/>
    <path fill="var(--paper)" d="M0 348 C75 432 262 418 432 397 C562 381 700 360 753 408 L753 429 L0 429 Z"/>
    <path fill="var(--brand-blue)" d="M0 353 C78 436 265 422 434 401 C564 385 702 366 753 413 L753 429 L0 429 Z"/>
  </svg>

  <div class="wordmark">
    <span class="wordmark__dot"></span>
    <span class="wordmark__text">
      <span class="wordmark__name">TALVEX</span>
      <span class="wordmark__tagline">INDUSTRIAL MAINTENANCE</span>
    </span>
  </div>

  <div class="divider"></div>

  <div class="contact">
    <p class="contact__name">Dale Virnow Jr.</p>
    <ul class="contact__list">
      <li class="contact__item">
        <svg class="contact__icon" viewBox="0 0 24 24" aria-hidden="true"><path d="M6.6 10.8a15 15 0 0 0 6.6 6.6l2.2-2.2c.3-.3.7-.4 1-.2 1.1.4 2.3.6 3.6.6.6 0 1 .4 1 1V20c0 .6-.4 1-1 1C10.6 21 3 13.4 3 4c0-.6.4-1 1-1h3.5c.6 0 1 .4 1 1 0 1.3.2 2.5.6 3.6.1.3 0 .7-.2 1z"/></svg>
        <span>413-627-8154</span>
      </li>
      <li class="contact__item">
        <svg class="contact__icon" viewBox="0 0 24 24" aria-hidden="true"><path d="M2 5h20v14H2z M4 7v.3l8 6 8-6V7l-8 6z" fill-rule="evenodd"/></svg>
        <span>dale.virnow.jr@brindlemail.net</span>
      </li>
      <li class="contact__item">
        <svg class="contact__icon" viewBox="0 0 24 24" aria-hidden="true"><circle cx="12" cy="12" r="10"/><path fill="var(--paper)" d="M7 6c2 0 3 1 3 3s-2 2-2 4 1 3 0 5c-2-1-4-4-4-6 0-3 1-5 3-6zm8 3c2 0 3 1 3 3s-1 4-3 5c0-2-1-3-1-5s0-3 1-3z"/></svg>
        <span>www.talvexindustrial.com</span>
      </li>
    </ul>
  </div>
</section>

<section class="card card--back" aria-label="Business card back">
  <div class="wordmark">
    <span class="wordmark__dot"></span>
    <span class="wordmark__text">
      <span class="wordmark__name">TALVEX</span>
      <span class="wordmark__tagline">INDUSTRIAL MAINTENANCE</span>
    </span>
  </div>
</section>

</body>
</html>
```